Corvella Foundation is a new grant making charity set up in the UK.

Having got a logo, we now need a website to go with it. We have worked out the text which people are going to need in order to then apply for grants. But having found out what we require they will probably need to go away and think about it.
We have to be careful of what images we use. So I have uploaded some images that we like. We are also going to be adding more pages almost immediately so need to think about the images for these.
I know basic wordpress so I will be able to add new pages/make alterations in future.
Updates
The website does need to be coded in Wordpress so that I can maintain it afterwards.
Marisse
Brief changed to provide more money and we have also provided more possible pictures. And generally more explanation.
Target Market(s)
departments in universities, other charities doing work on relief of pain, people working in health service departments
Industry/Entity Type
Health Charity
Coding
Coded - Design and coding required
Number of Pages Required
4 page
Look and feel
Each slider illustrates characteristics of the customer's brand and the style your logo design should communicate.

```html
<!DOCTYPE html>
<html lang="en">
<head>
<meta charset="utf-8">
<title>Corvella Foundation</title>
<link rel="stylesheet" href="https://fonts.googleapis.com/css2?family=Michroma&family=Montserrat:wght@500;600;700&family=Figtree:wght@400;500;700&display=swap">
<style>
:root{
  --blue:#1a5fc4;
  --blue-deep:#0a2d8f;
  --purple:#4a0f9e;
  --indigo:#2d1d9e;
  --orange:#f28a07;
  --ink:#2b2b3a;
  --grey:#4b4b58;
  --white:#ffffff;
  --field:#f7f8fb;
}
*{box-sizing:border-box;margin:0;padding:0}
html,body{width:1200px;height:3182px;overflow:hidden}
body{position:relative;background:var(--white);font-family:"Figtree",sans-serif;color:var(--ink)}
.abs{position:absolute}

/* header */
.site-header{left:0;top:0;width:1200px;height:82px;background:var(--white);border-bottom:1px solid #e6e6ea}
.brand{display:flex;align-items:center;gap:10px}
.brand-mark{width:36px;height:36px;background:var(--blue)}
.brand-name{font-family:"Montserrat",sans-serif;font-weight:700;color:var(--blue);font-size:21px;letter-spacing:.5px;line-height:1}
.site-header .brand{left:132px;top:23px}
.main-nav a{position:absolute;top:26px;font-family:"Montserrat",sans-serif;font-weight:500;font-size:14px;color:#222;text-decoration:none;letter-spacing:.3px}
.main-nav a.active{color:var(--blue)}
.main-nav a.active::after{content:"";position:absolute;left:-5px;right:-5px;top:30px;height:3px;background:var(--blue)}

/* hero */
.hero{left:0;top:93px;width:1200px;height:635px;overflow:hidden}
.hero-image{position:absolute;inset:0;background:radial-gradient(circle at 750px 270px,#5b6cff 0,#2452c8 90px,#0e2f86 260px,#06153d 520px),#06153d}
.hero-frame{left:136px;top:162px;width:430px;height:249px;border:4px solid var(--white);text-align:center;color:var(--white)}
.hero-frame h1{font-family:"Michroma",sans-serif;font-weight:400;font-size:43px;line-height:50px;margin-top:32px}
.hero-frame p{font-family:"Michroma",sans-serif;font-size:18px;line-height:27px;margin-top:10px}
.btn{display:block;background:var(--orange);color:var(--white);border-radius:24px;text-align:center;font-family:"Montserrat",sans-serif;font-weight:700}
.hero .btn{left:280px;top:388px;width:153px;height:44px;line-height:44px;font-size:13px;box-shadow:0 0 0 9px #0b2670}
.slider-arrow{width:40px;height:40px;border-radius:50%;background:var(--white);top:255px}

/* welcome */
.welcome-art{left:157px;top:805px;width:360px;height:360px;border-radius:50%;background:linear-gradient(180deg,#f4f6fb 0,#f4f6fb 40%,#c8862f 62%,#9b3a3a 100%);box-shadow:0 0 0 22px #f5f7fd,0 0 0 24px #e3e8f7,0 10px 40px 24px rgba(40,70,160,.08)}
.welcome h2{left:605px;top:862px;font-family:"Michroma",sans-serif;font-weight:400;font-size:28px;line-height:35px;color:var(--purple)}
.welcome h2 span{color:var(--blue)}
.rule{height:3px;width:60px;background:var(--blue)}
.welcome .rule{left:605px;top:939px}
.welcome-copy{left:607px;top:977px;width:440px;font-size:17px;line-height:28.5px;color:var(--grey)}
.welcome-copy p+p{margin-top:10px}

/* about */
.about{left:0;top:1245px;width:1200px;height:595px;background:radial-gradient(circle at 880px 300px,#2f6be0 0,#0d4ec4 260px,#0437a8 520px,#032a86 800px)}
.about h2{left:138px;top:120px;font-family:"Michroma",sans-serif;font-weight:400;font-size:28px;color:var(--white)}
.about .rule{left:138px;top:158px;background:var(--white);width:62px}
.faq{left:136px;top:196px;width:520px;color:var(--white)}
.faq-item{position:relative;padding-left:26px;font-family:"Montserrat",sans-serif;font-weight:600;font-size:14.5px;line-height:20px;margin-bottom:26px}
.faq-item::before{content:"+";position:absolute;left:0;top:-1px;font-weight:500;font-size:18px;opacity:.85}
.faq-item.open::before{content:"–"}
.faq-answer{font-family:"Figtree",sans-serif;font-weight:400;font-size:14px;line-height:24px;margin-top:12px;opacity:.95}
.about-art{left:699px;top:120px;width:360px;height:360px;border-radius:50%;background:radial-gradient(circle at 55% 45%,#7fc3ff 0,#2a8cf0 45%,#1050c8 100%);box-shadow:0 0 0 16px rgba(255,255,255,.05),0 0 0 18px rgba(255,255,255,.35),0 0 0 28px rgba(255,255,255,.04),0 0 0 30px rgba(255,255,255,.25)}

/* grants */
.grants{left:0;top:1840px;width:1200px;height:702px;background:linear-gradient(115deg,#fafbff 0,#eef0fb 55%,#d5d9f3 100%)}
.grants h2{left:0;width:1200px;top:78px;text-align:center;font-family:"Michroma",sans-serif;font-weight:400;font-size:30px;color:var(--indigo)}
.grants .rule{left:567px;top:126px;width:62px}
.grants-copy{left:180px;top:148px;width:840px;text-align:center;font-size:14.5px;line-height:19px;color:var(--grey)}
.grants-copy p{margin-bottom:17px}
.category{width:170px;text-align:center}
.category .icon{width:94px;height:94px;border-radius:50%;background:radial-gradient(circle at 40% 35%,#3b5ff0 0,#1e2fb8 70%,#1a23a0 100%);margin:0 auto;display:flex;align-items:center;justify-content:center}
.category h3{font-family:"Montserrat",sans-serif;font-weight:600;font-size:14px;line-height:19px;color:var(--indigo);margin-top:14px;text-transform:uppercase}
.grants-note{left:270px;top:572px;width:660px;text-align:center;font-size:14px;line-height:20px;color:var(--grey)}

/* contact */
.contact{left:0;top:2542px;width:1200px;height:640px;background:linear-gradient(100deg,#1e3be0 0,#2e2fd8 40%,#5a1fc8 75%,#6a1ab8 100%);overflow:hidden}
.contact h2{left:0;width:1200px;top:74px;text-align:center;font-family:"Michroma",sans-serif;font-weight:400;font-size:28px;color:var(--white)}
.contact .rule{left:569px;top:117px;width:62px;background:var(--white)}
.field{background:var(--field);display:flex;align-items:center;gap:10px;padding-left:18px;font-family:"Montserrat",sans-serif;font-size:13px;color:#555}
.field.message{align-items:flex-start;padding-top:14px}
.contact .btn{left:521px;top:333px;width:172px;height:44px;line-height:44px;font-size:16px;letter-spacing:.5px}
.footer-wave{left:0;top:390px;width:1200px;height:250px}
.site-footer .brand{left:480px;top:496px}
.footer-nav a{position:absolute;top:548px;font-family:"Montserrat",sans-serif;font-weight:500;font-size:14.5px;color:#222;text-decoration:none}
.copyright{left:0;width:1200px;top:582px;text-align:center;font-size:12px;color:#333}
</style>
</head>
<body>

<header class="site-header abs">
  <div class="brand abs"><span class="brand-mark"></span><span class="brand-name">CORVELLA FOUNDATION</span></div>
  <nav class="main-nav">
    <a class="active" style="left:540px">HOME</a>
    <a style="left:655px">ABOUT US</a>
    <a style="left:805px">GRANTS</a>
    <a style="left:938px">CONTACT US</a>
  </nav>
</header>

<section class="hero abs">
  <div class="hero-image" role="img" aria-label="Glowing blue nerve cell with orange light points on a dark background"></div>
  <div class="hero-frame abs">
    <h1>CORVELLA<br>FOUNDATION</h1>
    <p>WE REDUCE THE SUFFERING<br>CAUSED BY CHRONIC PAIN.</p>
  </div>
  <a class="btn abs">CONTACT US</a>
  <svg class="slider-arrow abs" style="left:28px" viewBox="0 0 40 40"><path d="M23 12 15 20l8 8" fill="none" stroke="#111" stroke-width="3"/></svg>
  <svg class="slider-arrow abs" style="left:1132px" viewBox="0 0 40 40"><path d="M17 12l8 8-8 8" fill="none" stroke="#111" stroke-width="3"/></svg>
</section>

<section class="welcome">
  <div class="welcome-art abs" role="img" aria-label="Illustration of a diverse crowd of people in warm colours"></div>
  <h2 class="abs">WELCOME TO CORVELLA<br><span>FOUNDATION</span></h2>
  <div class="rule abs"></div>
  <div class="welcome-copy abs">
    <p>Corvella Foundation is a grant making charity set up in the UK in 2021. The main aim of Corvella Foundation is to reduce the suffering caused by chronic pain.</p>
    <p>Charity registration number 1187356.</p>
  </div>
</section>

<section class="about abs" role="img" aria-label="Blue background with faint nerve cell imagery">
  <h2 class="abs">ABOUT US</h2>
  <div class="rule abs"></div>
  <div class="faq abs">
    <div class="faq-item open">Who are the trustees of Corvella Foundation?
      <div class="faq-answer">The initial trustees are Marisse, Tobias &amp; Lionel Hollister.<br>A fourth trustee is about to be appointed, the legal firm of Brandt Okafor.</div>
    </div>
    <div class="faq-item">Who are the medical advisers to Corvella Foundation?</div>
    <div class="faq-item">How much money does Corvella Foundation have?</div>
    <div class="faq-item">Where has this money come from?</div>
    <div class="faq-item">Why is the foundation named after Marisse Hollister?</div>
  </div>
  <div class="about-art abs" role="img" aria-label="Close-up of bright blue neurons with glowing synapses"></div>
</section>

<section class="grants abs" role="img" aria-label="Pale lavender background with faint neuron imagery">
  <h2 class="abs">CORVELLA GRANTS</h2>
  <div class="rule abs"></div>
  <div class="grants-copy abs">
    <p>Grants will almost entirely be provided for research or education into pain management, or the prevention of pain.</p>
    <p>The trustees will also be providing grants to a number of other charities or to areas with which they have had a long term association, such as HIV/AIDS and TB. There is no application procedure for these other areas, and unsolicited applications are unlikely to be favorably considered by the trustees</p>
    <p>The main categories of funding for pain research or education will be as follows.</p>
  </div>

  <div class="category abs" style="left:113px;top:352px">
    <div class="icon"><svg width="46" height="46" viewBox="0 0 46 46" fill="none" stroke="#fff" stroke-width="2.2" stroke-linecap="round"><circle cx="23" cy="23" r="4"/><path d="M20 20 10 10M26 20l10-8M26 26l11 6M20 26l-9 10M10 10l-4 2M10 10l1-5M36 12l4 2M37 32l4-2M11 36l-5-1"/></svg></div>
    <h3 style="margin-top:20px">Pain<br>Centres</h3>
  </div>
  <div class="category abs" style="left:268px;top:352px">
    <div class="icon"><svg width="40" height="46" viewBox="0 0 40 46" fill="#fff"><rect x="13" y="4" width="14" height="7" rx="1"/><rect x="10" y="13" width="20" height="28" rx="3"/><path d="M18 21h4v4h4v4h-4v4h-4v-4h-4v-4h4z" fill="#2538c0"/></svg></div>
    <h3>The use of<br>opioids</h3>
  </div>
  <div class="category abs" style="left:425px;top:352px">
    <div class="icon"><svg width="46" height="46" viewBox="0 0 46 46" fill="none" stroke="#fff" stroke-width="2.2" stroke-linecap="round"><path d="M14 40v-8c-4-3-6-7-6-12 0-8 7-14 15-14s15 6 15 14c0 3-1 5-3 7l3 5h-3v4c0 2-2 3-4 3h-4v1"/><path d="M18 20c0-3 2-5 5-5s5 2 5 5-2 4-5 4M23 24v4"/></svg></div>
    <h3>Improving the<br>use of medication</h3>
  </div>
  <div class="category abs" style="left:581px;top:352px">
    <div class="icon"><svg width="46" height="46" viewBox="0 0 46 46" fill="none" stroke="#fff" stroke-width="2.2" stroke-linejoin="round"><path d="M4 18 23 10l19 8-19 8z"/><path d="M12 22v9c3 3 7 4 11 4s8-1 11-4v-9"/></svg></div>
    <h3 style="margin-top:20px">Education</h3>
  </div>
  <div class="category abs" style="left:737px;top:352px">
    <div class="icon"><svg width="46" height="46" viewBox="0 0 46 46" fill="none" stroke="#fff" stroke-width="2.2" stroke-linejoin="round"><path d="M16 6 9 20h7l-4 12 12-16h-7l5-10zM33 14l-5 9h5l-3 8 8-11h-5l3-6z"/><path d="M8 38h30" stroke-linecap="round"/></svg></div>
    <h3>Improved<br>types of pain<br>control</h3>
  </div>
  <div class="category abs" style="left:894px;top:352px">
    <div class="icon"><svg width="46" height="46" viewBox="0 0 46 46" fill="none" stroke="#fff" stroke-width="2.2" stroke-linecap="round"><path d="M9 33a17 17 0 1 1 28 0"/><path d="M23 27l7-9"/><circle cx="23" cy="27" r="2.5" fill="#fff"/><path d="M13 20l2 1M23 11v2M33 20l-2 1"/></svg></div>
    <h3>Measuring<br>pain</h3>
  </div>

  <p class="grants-note abs">The trustees will initially consider unsolicited applications, for up to £50,000 each, in these areas or related areas. Applications for more substantial project funding will be invited in due course.</p>
</section>

<section class="contact abs">
  <h2 class="abs">CONTACT CORVELLA</h2>
  <div class="rule abs"></div>
  <div class="field abs" style="left:198px;top:144px;width:400px;height:49px"><svg width="16" height="16" viewBox="0 0 16 16" fill="none" stroke="#555" stroke-width="1.4"><circle cx="8" cy="5" r="3.2"/><path d="M2 15c0-3.5 2.7-5.5 6-5.5s6 2 6 5.5"/></svg>Name</div>
  <div class="field abs" style="left:198px;top:200px;width:400px;height:49px"><svg width="16" height="12" viewBox="0 0 16 12" fill="none" stroke="#555" stroke-width="1.4"><rect x="1" y="1" width="14" height="10"/><path d="M1 1l7 6 7-6"/></svg>E-mail address</div>
  <div class="field abs" style="left:198px;top:255px;width:400px;height:49px"><svg width="14" height="14" viewBox="0 0 14 14" fill="#555"><path d="M3 1l2.5 3-1.5 1.5c1 2 2.5 3.5 4.5 4.5L10 8.5 13 11l-2 2C6 12.5 1.5 8 1 3z"/></svg>Phone</div>
  <div class="field message abs" style="left:608px;top:144px;width:398px;height:160px">Message</div>
  <a class="btn abs">SUBMIT</a>

  <svg class="footer-wave abs" viewBox="0 0 1200 250" preserveAspectRatio="none">
    <path d="M0 92C300 -5 900 -5 1200 88V250H0z" fill="#fff"/>
    <path d="M0 92C300 -5 900 -5 1200 88" fill="none" stroke="#3d2cc8" stroke-width="5"/>
  </svg>
  <footer class="site-footer">
    <div class="brand abs"><span class="brand-mark"></span><span class="brand-name">CORVELLA FOUNDATION</span></div>
    <nav class="footer-nav">
      <a style="left:328px">HOME</a>
      <a style="left:451px">ABOUT US</a>
      <a style="left:609px">GRANTS</a>
      <a style="left:751px">CONTACT US</a>
    </nav>
    <p class="copyright abs">Copyright © 2021 Corvella Foundation &nbsp;|&nbsp; All Rights Reserved</p>
  </footer>
</section>

</body>
</html>
```